A bar in Newtown, NSW needs a website

We need a website design for a small speakeasy-style bar in Newtown, NSW Australia. The website needs to be simple to navigate, minimalistic, and feature light colours.

The functionality has to be fairly simple:

Main page (navigates to things below)
Food menu
Beverage menu
Bookings

Social media links and misc info at the bottom of every page.

The menus pages need to have space for text inserted as a jpeg file.

Name and logo are attached.

Coding

Coded - Design and coding required

Number of Pages Required

4 page

```html
<!DOCTYPE html>
<html lang="en">
<head>
<meta charset="utf-8">
<title>The Quiet Fox — Newtown Bar</title>
<link href="https://fonts.googleapis.com/css2?family=Roboto:wght@300;400;500;700;900&family=Roboto+Slab:wght@400;700&display=swap" rel="stylesheet">
<style>
:root{
  --red:#e14b4b;
  --red-dark:#c73b3b;
  --ink:#1e1e1e;
  --text:#333;
  --muted:#8a8a8a;
  --light:#efefef;
  --white:#fff;
  --night:#141414;
  --footer:#1b1b1b;
  --footer-bottom:#0f0f0f;
}
*{box-sizing:border-box;margin:0;padding:0}
html,body{width:1200px;height:4440px;overflow:hidden}
body{font-family:"Roboto",Arial,sans-serif;color:var(--text);background:var(--white);position:relative}
.abs{position:absolute}

/* Hero */
.hero{position:absolute;left:0;top:0;width:1200px;height:690px;
  background:radial-gradient(ellipse at 30% 40%,#3a2a1c 0%,#1a1410 45%,#0b0a09 100%);color:var(--white)}
.topbar{position:absolute;top:12px;left:96px;right:96px;height:24px;font-size:13px;display:flex;align-items:center;gap:30px}
.topbar .item{display:flex;align-items:center;gap:8px}
.socials{position:absolute;right:0;top:4px;display:flex;gap:22px}
.socials span{width:12px;height:12px;border-radius:50%;background:var(--red)}
.logo{position:absolute;left:480px;top:40px;width:240px;text-align:center;font-weight:700;font-size:34px;line-height:1;letter-spacing:1px;color:var(--white)}
.logo small{display:block;font-size:16px;letter-spacing:4px;margin-bottom:4px;font-weight:700}
.hero h1{position:absolute;left:110px;top:334px;font-weight:400;font-size:44px;letter-spacing:4px;line-height:1}
.hero h2{position:absolute;left:110px;top:392px;font-weight:700;font-size:62px;letter-spacing:1px;line-height:1}
.hero p{position:absolute;left:110px;top:470px;font-size:30px;font-weight:400}
.hero-glass{position:absolute;left:800px;top:60px;width:220px;height:600px;
  background:linear-gradient(180deg,rgba(80,40,10,.2) 0%,#7a3d12 45%,#b8641f 70%,#5a2c0e 100%);
  border-radius:10px 10px 30px 30px;opacity:.9}

/* Nav */
.nav{position:absolute;top:690px;left:0;width:1200px;height:78px;background:var(--red)}
.nav a{position:absolute;top:24px;height:30px;line-height:30px;color:var(--white);font-size:15px;font-weight:500;text-decoration:none;letter-spacing:.5px}
.nav a.active{background:rgba(255,255,255,.3);padding:0 18px}

/* Section titles */
.title{position:absolute;left:0;width:1200px;text-align:center;font-weight:900;font-size:44px;color:var(--ink);line-height:1}
.subtitle{position:absolute;left:0;width:1200px;text-align:center;font-size:16px;color:var(--text)}
.rule{position:absolute;left:562px;width:76px;height:3px;background:var(--red)}
.on-dark{color:var(--white)}

/* Story */
.story-photo{position:absolute;border-radius:50%;background:radial-gradient(circle at 40% 40%,#b5632b,#4a2411 70%,#22130b)}
.story-text{position:absolute;left:561px;top:1040px;width:550px;font-size:13.5px;line-height:1.55;color:#444}
.story-text p{margin-bottom:14px}
.btn{position:absolute;background:var(--red);color:var(--white);font-size:12px;font-weight:500;text-align:center;letter-spacing:.5px}

/* Beers */
.beers{position:absolute;left:0;top:1446px;width:1200px;height:705px;background:var(--light)}
.beers .lead{position:absolute;left:210px;width:780px;top:110px;text-align:center;font-size:16px;line-height:1.6;color:#444}
.beer{position:absolute;top:240px;width:300px;text-align:center}
.beer .photo{margin:0 auto;width:200px;height:258px;background:linear-gradient(180deg,#fff8e6 0%,#f1b642 35%,#c47c1b 80%,#a57a4a 100%);border-radius:20px 20px 60px 60px}
.beer h3{margin-top:30px;font-size:15px;font-weight:700;color:var(--ink)}
.beer p{margin-top:14px;font-size:12.5px;line-height:1.7;color:var(--muted)}

/* Menu board */
.board{position:absolute;left:135px;top:2385px;width:936px;height:330px}
.menu-col{position:absolute;top:2440px;width:270px;color:var(--white)}
.menu-col h3{text-align:center;font-size:22px;font-weight:700;margin-bottom:30px}
.menu-item{font-size:12px;margin-bottom:20px}
.menu-item .row{display:flex;align-items:baseline;gap:6px}
.menu-item .dots{flex:1;border-bottom:1px dashed rgba(255,255,255,.6)}
.menu-item small{display:block;font-size:10px;color:#bbb;margin-top:3px}
.board-name{position:absolute;left:450px;top:2470px;width:300px;text-align:center;color:var(--white);font-weight:700;font-size:40px;line-height:1}
.board-name small{display:block;font-size:18px;letter-spacing:4px;margin-bottom:4px}

/* Booking */
.booking{position:absolute;left:0;top:2835px;width:1200px;height:504px;background:linear-gradient(180deg,#2b2622 0%,#3e3630 50%,#241f1b 100%)}
.booking .lead{position:absolute;left:210px;width:780px;top:124px;text-align:center;font-size:16px;line-height:1.6;color:var(--white)}
.form{position:absolute;left:96px;top:255px;width:1002px;height:120px;background:var(--white)}
.field{position:absolute;top:42px;height:34px;border:1px solid #ddd;font-size:12px;color:#777;display:flex;align-items:center;padding-left:34px}
.form .note{position:absolute;left:64px;top:94px;font-size:11px;color:#555}

/* Testimonials */
.testi-name{position:absolute;left:0;width:1200px;top:3580px;text-align:center;font-family:"Roboto Slab",serif;font-weight:700;font-size:20px;color:var(--ink)}
.testi-quote{position:absolute;left:240px;width:720px;top:3622px;text-align:center;font-size:20px;line-height:1.5;color:#222}
.avatar{position:absolute;left:543px;top:3747px;width:114px;height:114px;border-radius:50%;background:radial-gradient(circle,#e7b79a,#b4572f)}

/* Footer */
.footer{position:absolute;left:0;top:4008px;width:1200px;height:372px;background:var(--footer);color:#ccc}
.fcol{position:absolute;top:50px;font-size:12px;line-height:1.7}
.fcol h4{color:var(--red);font-size:15px;font-weight:700;margin-bottom:26px;letter-spacing:.5px}
.fcol .line{display:flex;gap:10px;align-items:center;margin-bottom:10px}
.fsoc{display:flex;gap:10px;margin-top:26px}
.fsoc span{width:22px;height:22px;border-radius:50%;border:1px solid var(--red)}
.hours{display:grid;grid-template-columns:110px 1fr;row-gap:10px}
.search{display:flex;margin-top:20px}
.search .input{width:160px;height:32px;background:var(--white);font-size:11px;color:#999;padding:8px}
.search .go{width:44px;height:32px;background:var(--red)}
.copyright{position:absolute;left:0;top:4380px;width:1200px;height:60px;background:var(--footer-bottom);color:#ddd;font-size:13px;text-align:center;line-height:60px}
</style>
</head>
<body>

<header class="hero">
  <div class="topbar">
    <span class="item"><svg width="14" height="10" viewBox="0 0 14 10"><rect x=".5" y=".5" width="13" height="9" fill="none" stroke="#fff"/><path d="M1 1l6 5 6-5" fill="none" stroke="#fff"/></svg>hello@quietfox.example</span>
    <span class="item"><svg width="12" height="12" viewBox="0 0 12 12"><path d="M2 1l2 0 1 3-1.5 1a7 7 0 003.5 3.5L8 7l3 1v2a1 1 0 01-1 1A10 10 0 011 2a1 1 0 011-1z" fill="#fff"/></svg>(02) 5550 0142</span>
    <div class="socials"><span></span><span></span><span></span><span></span><span></span></div>
  </div>
  <div class="logo"><small>THE</small>QUIET FOX</div>
  <div class="hero-glass" role="img" aria-label="Whisky glass with ice being filled"></div>
  <h1>WELCOME TO</h1>
  <h2>OUR RESTURTANT</h2>
  <p>We Brings You Healthy Foods</p>
</header>

<nav class="nav">
  <a class="active" style="left:220px">HOME</a>
  <a style="left:354px">FOOD MENU</a>
  <a style="left:516px">BEVERAGE MENU</a>
  <a style="left:714px">BOOKINGS</a>
  <a style="left:866px">CONTACT US</a>
</nav>

<section class="story">
  <h2 class="title" style="top:838px">OUR STORY</h2>
  <p class="subtitle" style="top:898px">A little about us and a breif history of how we started.</p>
  <div class="rule" style="top:938px"></div>
  <div class="story-photo" style="left:171px;top:1005px;width:282px;height:282px" role="img" aria-label="Warm-lit bar interior"></div>
  <div class="story-photo" style="left:132px;top:1170px;width:120px;height:120px;border:5px solid #fff" role="img" aria-label="Bartender pouring a drink"></div>
  <div class="story-photo" style="left:306px;top:1200px;width:140px;height:140px;border:5px solid #fff;background:radial-gradient(circle,#d99a34,#6a3a14)" role="img" aria-label="Glasses of beer on a table"></div>
  <div class="story-text">
    <p>We opened our doors on a quiet corner of King Street with one small bar, a handful of stools and a love for well made drinks. Friends came for a pint and stayed for the stories, and soon the room filled every night with neighbours.</p>
    <p>Our kitchen grew slowly, dish by dish, built on simple food cooked with care. We still source from local growers and brewers, and we still pour every drink by hand the way we did on the very first night.</p>
    <p>Today we are a small home for Newtown, warm, relaxed and always open for one more round with good company and good music.</p>
  </div>
  <div class="btn" style="left:576px;top:1314px;width:111px;height:36px;line-height:36px">READ MORE</div>
</section>

<section class="beers">
  <h2 class="title" style="top:52px">JOIN US FOR A BEER!</h2>
  <p class="lead">At our pub, we proudly offer our guests to taste our best types of beer brewed from carefully selected barley, wheat and hops. Take a look below to learn more about our best beers.</p>
  <div class="rule" style="top:182px"></div>
  <div class="beer" style="left:129px"><div class="photo" role="img" aria-label="Mug of frothy lager"></div><h3>HARBOUR GOLD - LANE LAGER</h3><p>Crisp and light with a soft honey finish.<br>Brewed nearby and poured fresh daily,<br>best enjoyed with friends on the terrace.</p></div>
  <div class="beer" style="left:450px"><div class="photo" role="img" aria-label="Two tall glasses of pale ale"></div><h3>HARBOUR GOLD - LANE LAGER</h3><p>Crisp and light with a soft honey finish.<br>Brewed nearby and poured fresh daily,<br>best enjoyed with friends on the terrace.</p></div>
  <div class="beer" style="left:801px"><div class="photo" style="background:linear-gradient(180deg,#eee 0%,#2a1306 25%,#5a2a0c 60%,#a57a4a 100%)" role="img" aria-label="Glass of dark amber ale"></div><h3>HARBOUR GOLD - LANE LAGER</h3><p>Crisp and light with a soft honey finish.<br>Brewed nearby and poured fresh daily,<br>best enjoyed with friends on the terrace.</p></div>
</section>

<section class="menu">
  <h2 class="title" style="top:2218px">OUR MENU</h2>
  <p class="subtitle" style="top:2278px">A little about us and a breif history of how we started.</p>
  <div class="rule" style="top:2318px"></div>
  <svg class="board" viewBox="0 0 936 330" aria-hidden="true">
    <defs><linearGradient id="wood" x1="0" y1="0" x2="0" y2="1"><stop offset="0" stop-color="#2e2e2e"/><stop offset="1" stop-color="#141414"/></linearGradient></defs>
    <path d="M10 45 H315 Q330 5 360 0 H576 Q606 5 621 45 H926 V265 H621 Q606 315 576 325 H360 Q330 315 315 265 H10 Z" fill="url(#wood)"/>
    <path d="M22 57 H322 Q336 20 362 13 H574 Q600 20 614 57 H914 V253 H614 Q600 300 574 312 H362 Q336 300 322 253 H22 Z" fill="none" stroke="#777" stroke-dasharray="4 4"/>
  </svg>
  <div class="board-name"><small>THE</small>QUIET FOX</div>
  <div class="menu-col" style="left:180px">
    <h3>FOOD</h3>
    <div class="menu-item"><div class="row">LANE FRITTERS<span class="dots"></span>13.00</div><small>Soup / Lemon / Garlic</small></div>
    <div class="menu-item"><div class="row">LANE FRITTERS<span class="dots"></span>13.00</div><small>Soup / Lemon / Garlic</small></div>
    <div class="menu-item"><div class="row">LANE FRITTERS<span class="dots"></span>13.00</div><small>Soup / Lemon / Garlic</small></div>
  </div>
  <div class="menu-col" style="left:750px">
    <h3>BEVERAGE</h3>
    <div class="menu-item"><div class="row">THE NIGHT OWL<span class="dots"></span>10.00</div><small>Irish Cream, Whiskey, Orange Liqueur</small></div>
    <div class="menu-item"><div class="row">THE NIGHT OWL<span class="dots"></span>10.00</div><small>Irish Cream, Whiskey, Orange Liqueur</small></div>
    <div class="menu-item"><div class="row">THE NIGHT OWL<span class="dots"></span>10.00</div><small>Irish Cream, Whiskey, Orange Liqueur</small></div>
  </div>
</section>

<section class="booking" role="img" aria-label="Blurred dining room with warm lights">
  <h2 class="title on-dark" style="top:60px">BOOK A TABLE</h2>
  <p class="lead">At our pub, we proudly offer our guests to taste our best types of beer brewed from carefully selected barley, wheat and hops. Take a look below to learn more about our best beers.</p>
  <div class="rule" style="top:204px"></div>
  <div class="form">
    <div class="field" style="left:16px;width:250px">03/14/2024</div>
    <div class="field" style="left:290px;width:200px">7:00pm</div>
    <div class="field" style="left:556px;width:200px">2 Person</div>
    <div class="btn" style="left:843px;top:40px;width:129px;height:38px;line-height:38px;font-size:13px">Book a Table</div>
    <p class="note">Call (02) 5550 0142 from 5am – 11pm daily, or book online with ease. Reservations required for parties of 6 or more.</p>
  </div>
</section>

<section class="testimonials">
  <h2 class="title" style="top:3418px">TESTIMONIALS</h2>
  <p class="subtitle" style="top:3478px">A little about us and a breif history of how we started.</p>
  <div class="rule" style="top:3518px"></div>
  <p class="testi-name">Mara L.</p>
  <p class="testi-quote">"Standardized content uniquely myocardinate next-generation processes rather than long-term high-impact. Interactively transform effective content through multimedia"</p>
  <svg class="abs" style="left:238px;top:3744px" width="14" height="24" viewBox="0 0 14 24"><path d="M12 2L2 12l10 10" fill="none" stroke="#111" stroke-width="3"/></svg>
  <svg class="abs" style="left:942px;top:3744px" width="14" height="24" viewBox="0 0 14 24"><path d="M2 2l10 10L2 22" fill="none" stroke="#111" stroke-width="3"/></svg>
  <div class="avatar" role="img" aria-label="Guest portrait"></div>
</section>

<footer class="footer">
  <div class="fcol" style="left:96px;width:200px">
    <h4 style="text-align:center">ABOUT US</h4>
    <p>A small Newtown bar with good drinks, honest food and live music on weekends. Drop by after work or stay late with friends. Walk-ins are always welcome here.</p>
    <div class="fsoc"><span></span><span></span><span></span><span></span><span></span></div>
  </div>
  <div class="fcol" style="left:378px;width:200px">
    <h4>OUR CONTACT</h4>
    <div class="line"><svg width="10" height="14" viewBox="0 0 10 14"><path d="M5 0a5 5 0 015 5c0 4-5 9-5 9S0 9 0 5a5 5 0 015-5z" fill="#fff"/><circle cx="5" cy="5" r="2" fill="#1b1b1b"/></svg><span>Nell Harlow<br>Venue Manager<br>King Street Hospitality Group</span></div>
    <div class="line"><svg width="12" height="12" viewBox="0 0 12 12"><path d="M2 1l2 0 1 3-1.5 1a7 7 0 003.5 3.5L8 7l3 1v2a1 1 0 01-1 1A10 10 0 011 2a1 1 0 011-1z" fill="#fff"/></svg>02 5550 0187</div>
    <div class="line"><svg width="14" height="10" viewBox="0 0 14 10"><rect width="14" height="10" fill="#fff"/><path d="M0 0l7 5 7-5" fill="none" stroke="#1b1b1b"/></svg>nell@quietfox.example</div>
  </div>
  <div class="fcol" style="left:627px;width:200px">
    <h4>OPENING HOURS</h4>
    <div class="hours"><span>Monday</span><span>Closed</span><span>Tue-Fri</span><span>10 am - 12 pm</span><span>Sat-Sun</span><span>8 am - 11 pm</span><span>Holidays</span><span>8 am - 11 pm</span></div>
  </div>
  <div class="fcol" style="left:870px;width:220px">
    <h4 style="padding-left:60px">SEARCH</h4>
    <p>Find a dish, a drink or an event on our site. Type a word below and press the button to search.</p>
    <div class="search"><div class="input">Search...</div><div class="go"><svg width="44" height="32" viewBox="0 0 44 32"><circle cx="21" cy="15" r="5" fill="none" stroke="#fff" stroke-width="2"/><path d="M25 19l4 4" stroke="#fff" stroke-width="2"/></svg></div></div>
  </div>
</footer>
<div class="copyright">Copyright © 2016. All Rights Reserved.</div>

</body>
</html>
```